Business logo & card design needed

We need a business logo & card design for a new company in NSW called 'Tallow Ridge Solutions'.
The company provides electrical services such as; electrical/refrigeration & air conditioning/data/security/audio visual entertainment/design & install.
We would like a logo which can relate to the electrical industry.
Updates

Industry/Entity Type

Electrical

Contact Information for Business Card

Tallow Ridge Solutions
Lira Mostfeld, Ph: 0471958360, Lic: 562930K

Logo Text

Tallow Ridge Solutions

Logo styles of interest
Emblem Logo
Abstract Logo
Wordmark Logo
Requirements
Must have
• The card must include the services we provide; electrical/refrigeration & air conditioning/data/security/audio visual entertainment/design & install.
It must also include the licence number; Lic: 562930K

```html
<!DOCTYPE html>
<html lang="en">
<head>
<meta charset="utf-8">
<title>Tallow Ridge Solutions – Business Card</title>
<link rel="stylesheet" href="https://fonts.googleapis.com/css2?family=Oswald:wght@300;400;600&display=swap">
<style>
  :root {
    --stage: #333333;
    --card-edge: #dcdcdd;
    --card-face: #ffffff;
    --band: #231f20;
    --brand-purple: #5e2a84;
    --brand-gold: #fcc012;
    --band-text: #ffffff;
    --fine-print: #9a9a9a;
  }
  html, body {
    margin: 0;
    padding: 0;
    width: 985px;
    height: 1200px;
    overflow: hidden;
    background: var(--stage);
    font-family: "Oswald", "Arial Narrow", sans-serif;
  }
  .canvas {
    position: relative;
    width: 985px;
    height: 1200px;
  }
  .card {
    position: absolute;
    left: 137px;
    width: 662px;
    height: 370px;
    background: var(--card-edge);
  }
  .card--front { top: 140px; }
  .card--back  { top: 639px; }
  .card__face {
    position: absolute;
    left: 25px; right: 23px;
    top: 23px; bottom: 20px;
    background: var(--card-face);
  }
  .brand {
    position: absolute;
    left: 0; right: 0;
    top: 24px;
    display: flex;
    flex-direction: column;
    align-items: center;
    color: var(--brand-purple);
    font-weight: 400;
    line-height: 1;
  }
  .brand__mark {
    width: 46px;
    height: 46px;
    background: var(--brand-gold);
    margin-bottom: 22px;
  }
  .brand__name {
    font-size: 44px;
    letter-spacing: 2px;
    text-transform: uppercase;
    text-align: center;
  }
  .brand__name span {
    display: block;
    font-size: 32px;
    letter-spacing: 3px;
    margin-top: 6px;
  }
  .band {
    position: absolute;
    left: 0; right: 0;
    top: 264px;
    height: 65px;
    background: var(--band);
    color: var(--band-text);
  }
  .band--contact {
    display: flex;
    align-items: center;
    font-size: 25px;
    letter-spacing: 0.5px;
  }
  .contact__name {
    position: absolute;
    left: 93px;
    font-weight: 600;
    text-transform: uppercase;
    font-size: 23px;
  }
  .contact__phone {
    position: absolute;
    left: 400px;
    font-weight: 300;
  }
  .band--services {
    top: 256px;
    display: flex;
    flex-direction: column;
    justify-content: center;
    align-items: center;
    font-size: 19px;
    font-weight: 300;
    line-height: 1.35;
    text-transform: uppercase;
  }
  .services__line { white-space: nowrap; }
  .services__dot {
    color: var(--brand-gold);
    font-size: 10px;
    vertical-align: 3px;
    margin: 0 3px;
  }
  .licence {
    position: absolute;
    right: 32px;
    bottom: 32px;
    font-size: 13px;
    font-weight: 300;
    color: var(--fine-print);
    letter-spacing: 0.5px;
  }
</style>
</head>
<body>
<main class="canvas">

  <section class="card card--front" aria-label="Card front">
    <div class="card__face"></div>
    <div class="brand">
      <div class="brand__mark"></div>
      <div class="brand__name">Tallow Ridge<span>Solutions</span></div>
    </div>
    <div class="band band--contact">
      <span class="contact__name">Lira Mostfeld</span>
      <span class="contact__phone">PH: 04 7195 8360</span>
    </div>
  </section>

  <section class="card card--back" aria-label="Card back">
    <div class="card__face"></div>
    <div class="brand">
      <div class="brand__mark"></div>
      <div class="brand__name">Tallow Ridge<span>Solutions</span></div>
    </div>
    <div class="band band--services">
      <div class="services__line"><span class="services__dot">◆</span>Electrical<span class="services__dot">◆</span>Refrigeration &amp; Air Conditioning<span class="services__dot">◆</span>Data<span class="services__dot">◆</span>Security<span class="services__dot">◆</span></div>
      <div class="services__line"><span class="services__dot">◆</span>Audio Visual Entertainment<span class="services__dot">◆</span>Design &amp; Install<span class="services__dot">◆</span></div>
    </div>
    <div class="licence">LIC: 562930K</div>
  </section>

</main>
</body>
</html>
```